IT Company requires new Business Card design.

Over the years we have had a few different business card designs. We are now due for new cards across the board for all staff. We felt this would be a good time to start fresh with a new design. Our traditional card simply had our details on the front, and a list of services on the back. We don't particularly need the list of services, we have had cards where the only thing on the rear of the card was our logo.
Feel free to be creative, we would like our tag line "Complete IT Management" to appear at some point, doesn't necessarily have to be with the logo.
I have attached samples and drafts of various previous cards we have used over the years.

```html
<!DOCTYPE html>
<html lang="en">
<head>
<meta charset="utf-8">
<title>Harbour Networking business card</title>
<link href="https://fonts.googleapis.com/css2?family=Arimo:ital,wght@0,400;0,700;1,400&display=swap" rel="stylesheet">
<style>
  :root {
    --navy-deep: #061a4a;
    --navy: #0a2f7a;
    --blue: #0e4fb8;
    --blue-bright: #1a7fe0;
    --cyan: #3cc8f4;
    --glow: #8fdcff;
    --grey-text: #c9ced8;
    --white: #ffffff;
    --ink: #000000;
  }
  * { margin: 0; padding: 0; box-sizing: border-box; }
  html, body { width: 964px; height: 1200px; overflow: hidden; background: var(--white); }
  body { position: relative; font-family: "Arimo", Arial, sans-serif; }

  .card {
    position: absolute; left: 0; width: 964px; height: 544px; overflow: hidden;
    background: radial-gradient(ellipse at 85% 70%, var(--blue) 0%, var(--navy) 45%, var(--navy-deep) 100%);
  }
  .card--front { top: 0; }
  .card--back { top: 603px; }

  .top-band {
    position: absolute; left: 0; top: 0; width: 100%; height: 158px;
    background: linear-gradient(90deg, #0f57c8 0%, #0b45a8 50%, #082e7a 100%);
  }
  .card--back .top-band { height: 115px; }

  .swirl {
    position: absolute; right: 0; top: 40px; width: 760px; height: 470px;
    background: radial-gradient(ellipse at 80% 75%, rgba(143,220,255,.55) 0%, rgba(60,160,240,.35) 30%, rgba(20,90,200,0) 70%);
  }

  .header-shape { position: absolute; left: 0; top: 0; }
  .header-title {
    position: absolute; left: 13px; color: var(--cyan); font-weight: 700;
    text-shadow: 0 0 6px rgba(0,0,0,.5);
  }
  .card--front .header-title { top: 116px; font-size: 37px; }
  .card--back .header-title { top: 119px; font-size: 33px; }

  .brand {
    position: absolute; left: 640px; top: 80px; width: 260px;
    display: flex; align-items: center; gap: 14px;
    color: var(--glow); font-weight: 700; font-size: 30px; line-height: 1.1;
  }
  .brand-square { width: 46px; height: 46px; background: var(--glow); flex: none; }

  .person-name {
    position: absolute; left: 32px; top: 208px; color: var(--grey-text);
    font-size: 50px; font-weight: 700; letter-spacing: 1px;
  }
  .mobile { position: absolute; left: 32px; top: 262px; color: var(--grey-text); font-size: 26px; font-weight: 700; }

  .contact { position: absolute; left: 32px; top: 393px; color: var(--grey-text); font-size: 26px; line-height: 33px; font-weight: 700; }
  .contact .email { font-weight: 400; font-style: italic; }

  .address {
    position: absolute; right: 45px; top: 303px; text-align: right;
    color: var(--grey-text); font-size: 27px; line-height: 33px; font-weight: 700;
    text-shadow: 0 0 4px rgba(0,0,0,.6);
  }

  .tagline-band { position: absolute; left: 0; bottom: 0; }
  .tagline {
    position: absolute; right: 30px; bottom: 8px; color: var(--cyan);
    font-size: 31px; font-weight: 700; text-shadow: 0 0 5px rgba(0,0,0,.5);
  }

  .services { position: absolute; top: 208px; color: var(--grey-text); font-size: 31px; line-height: 39px; list-style: none; }
  .services--left { left: 38px; }
  .services--right { left: 310px; }

  .bottom-strip {
    position: absolute; left: 0; bottom: 0; width: 100%; height: 46px;
    background: linear-gradient(90deg, #0d56c4, #1a78dc);
  }

  .side-label {
    position: absolute; left: 0; width: 964px; text-align: center;
    color: var(--ink); font-size: 32px; font-weight: 700;
  }
  .side-label--front { top: 553px; left: -30px; }
  .side-label--back { top: 1162px; left: -25px; }
</style>
</head>
<body>

<section class="card card--front">
  <div class="top-band"></div>
  <div class="swirl" role="img" aria-label="Flowing light-blue light streak illustration"></div>
  <svg class="header-shape" width="964" height="158" viewBox="0 0 964 158">
    <polygon points="0,158 0,112 490,112 444,158" fill="#0b3a94" opacity=".9"/>
  </svg>
  <h1 class="header-title">HARBOUR NETWORKING</h1>

  <div class="brand"><span class="brand-square"></span><span>Harbour Networking</span></div>

  <h2 class="person-name">DANIEL REEVES</h2>
  <p class="mobile">0412 555 018</p>

  <p class="contact">p 08 5550 1230<br>f 08 5550 1232<br><span class="email">daniel@harbournetworking.com.au</span></p>

  <p class="address">Unit 7<br>32 Corella Way<br>Hillview WA 6100<br>www.harbournetworking.com.au</p>

  <svg class="tagline-band" width="964" height="46" viewBox="0 0 964 46">
    <polygon points="465,46 510,0 964,0 964,46" fill="#1572d8"/>
  </svg>
  <p class="tagline">“Complete IT Management”</p>
</section>
<p class="side-label side-label--front">FRONT</p>

<section class="card card--back">
  <div class="top-band"></div>
  <div class="swirl" role="img" aria-label="Flowing light-blue light streak illustration"></div>
  <svg class="header-shape" width="964" height="158" viewBox="0 0 964 158">
    <polygon points="0,158 0,115 330,115 285,158" fill="#0b3a94" opacity=".9"/>
  </svg>
  <h2 class="header-title">We specialise in:</h2>

  <ul class="services services--left">
    <li>Hosting</li><li>Firewalls</li><li>Consumables</li><li>Servers</li><li>Racks</li>
  </ul>
  <ul class="services services--right">
    <li>Workstations</li><li>Laptops</li><li>Printers</li><li>Cabling/Electrical</li>
  </ul>

  <div class="bottom-strip"></div>
</section>
<p class="side-label side-label--back">BACK</p>

</body>
</html>
```